Restaurant menu design

Design fine dinning menu for Indian restaurant. Restaurant location is on river side. So if design has some touch of Yarra river of Melbourne and Indian touch. It is not compulsory. Creative and modern design is required.
I want to print in A3 and folded take away sizes so design should for both.
1. In A3, backside we need to design drink menu. I am attaching our current restaurant menu for drinks name and price.

Target Market(s)

Indian / Australian Customer

Industry/Entity Type

Indian Food, Indian fine dining

Colors
F0912C
F2A743
F7CA91
FBE8D2
FDF5EE

Requirements
Must have
• Simple but district design
Should not have
• common other restaurant type menu. Too many colours.

```html
<!DOCTYPE html>
<html lang="en">
<head>
<meta charset="utf-8">
<title>Tulsi's Kitchen – Menu</title>
<link href="https://fonts.googleapis.com/css2?family=Fira+Sans:wght@400;600&display=swap" rel="stylesheet">
<style>
  :root{
    --backdrop:#dcdcdc;
    --paper:#ffffff;
    --ink:#222222;
    --leaf:#3b5323;
    --chilli:#8b1c1c;
    --curry-leaf:#3e5a2b;
    --on-dark:#ffffff;
  }
  *{box-sizing:border-box}
  html,body{margin:0;padding:0;width:1029px;height:1200px;overflow:hidden;background:var(--backdrop);
    font-family:"Fira Sans",Arial,sans-serif;color:var(--ink)}
  .sheet{position:absolute;left:99px;width:830px;height:580px;background:var(--paper);overflow:hidden}
  .sheet--front{top:13px}
  .sheet--inside{top:607px}

  .col{position:absolute}
  .menu-section{margin:0 0 0 0}
  .menu-section h2{margin:0 0 7px;font-size:10px;font-weight:600;color:var(--leaf);letter-spacing:.1px}
  .item{margin:0 0 7px}
  .item__line{display:flex;align-items:baseline;width:74%;font-size:7.5px;font-weight:600;line-height:1.2;white-space:nowrap}
  .item__leader{flex:1;border-bottom:1px dotted currentColor;margin:0 1px;transform:translateY(-2px);min-width:6px}
  .item__desc{margin:1px 0 0;font-size:7px;line-height:1.3;font-weight:400}
  .plain .item__line{font-weight:400}

  /* front sheet */
  .hero-photo{position:absolute;left:240px;top:0;width:590px;height:580px;
    background:
      radial-gradient(ellipse 180px 160px at 88% 12%, rgba(70,110,40,.85), rgba(70,110,40,0) 70%),
      radial-gradient(circle 30px at 96% 49%, #c2332a 0%, #c2332a 90%, rgba(194,51,42,0) 100%),
      linear-gradient(90deg,#ffffff 0%,#f6efe5 20%,#e8d6bb 44%,#c69d68 60%,#7a5634 78%,#2f2b24 100%)}
  .brand{position:absolute;left:560px;top:208px;margin:0;font-size:58px;line-height:.98;font-weight:600;color:var(--on-dark);letter-spacing:.5px}

  /* inside sheet */
  .panel-chilli{position:absolute;left:0;top:0;width:276px;height:280px;background:var(--chilli);border-bottom-right-radius:30px}
  .panel-leaf{position:absolute;left:554px;top:216px;width:276px;height:364px;background:var(--curry-leaf);border-top-left-radius:30px}
  .on-dark,.on-dark h2{color:var(--on-dark)}
  .snack-photo{position:absolute;left:280px;top:164px;width:215px;height:143px;
    background:radial-gradient(ellipse 80px 45px at 38% 62%,#d9a55a,#c48a42 60%,rgba(196,138,66,0) 100%),
      linear-gradient(135deg,#f2ede6,#e4ddd2)}
</style>
</head>
<body>

<section class="sheet sheet--front">
  <div class="hero-photo" role="img" aria-label="Grilled kebab skewers on a wooden board with fresh coriander, tomato and spices"></div>
  <h1 class="brand">Tulsi's<br>Kitchen</h1>

  <div class="col" style="left:18px;top:66px;width:250px">
    <div class="menu-section">
      <h2>Non-Vegetarian Mains</h2>
      <div class="item"><div class="item__line"><span>Raja Rani Chicken</span><span class="item__leader"></span><span>$35</span></div>
        <p class="item__desc">Char-grilled chicken tikka wrapped in a silky egg roll, layered with makhani sauce &amp; spinach gravy – regal flavours in every bite.</p></div>
      <div class="item"><div class="item__line"><span>Butter Chicken</span><span class="item__leader"></span><span>$29</span></div>
        <p class="item__desc">A refined Delhi classic: chicken simmered in a tomato-butter sauce, smoky &amp; velvety.</p></div>
      <div class="item"><div class="item__line"><span>Lamb Rogan Josh</span><span class="item__leader"></span><span>$29</span></div>
        <p class="item__desc">Kashmiri-style lamb curry, slow-braised in aromatic spices with a deep, rich flavour.</p></div>
      <div class="item"><div class="item__line"><span>Dhaba Goat Masala</span><span class="item__leader"></span><span>$29</span></div>
        <p class="item__desc">A rustic North Indian goat curry, slow-cooked with onions, garlic, and earthy spices – inspired by India's iconic roadside kitchens.</p></div>
    </div>
  </div>

  <div class="col plain" style="left:18px;top:292px;width:250px">
    <div class="menu-section">
      <h2>Rice &amp; Biryanis</h2>
      <div class="item"><div class="item__line"><span>Plain Basmati Rice</span><span class="item__leader"></span><span>$8</span></div><p class="item__desc">Steamed long-grain basmati rice, light &amp; fluffy.</p></div>
      <div class="item"><div class="item__line"><span>Jeera Rice</span><span class="item__leader"></span><span>$8</span></div><p class="item__desc">Basmati rice tempered with roasted cumin seeds.</p></div>
      <div class="item"><div class="item__line"><span>Lemon Coconut Rice</span><span class="item__leader"></span><span>$10</span></div><p class="item__desc">Fragrant rice infused with lemon zest, curry leaves &amp; coconut.</p></div>
      <div class="item"><div class="item__line"><span>Peas Pulao</span><span class="item__leader"></span><span>$10</span></div><p class="item__desc">Delicate basmati rice cooked with sweet garden peas &amp; whole spices.</p></div>
      <div class="item"><div class="item__line"><span>Biryani Flavoured Rice</span><span class="item__leader"></span><span>$15</span></div><p class="item__desc">Aromatic saffron basmati rice prepared in biryani style.</p></div>
      <div class="item"><div class="item__line"><span>Vegetable Dum Biryani</span><span class="item__leader"></span><span>$28</span></div><p class="item__desc">Classic layered vegetable biryani with saffron, slow-cooked dum style.</p></div>
      <div class="item"><div class="item__line"><span>Hyderabadi Chicken Biryani</span><span class="item__leader"></span><span>$30</span></div><p class="item__desc">Fragrant rice layered with marinated chicken, spices &amp; saffron, served with raita.</p></div>
      <div class="item"><div class="item__line"><span>Lamb Dum Biryani</span><span class="item__leader"></span><span>$33</span></div><p class="item__desc">A celebratory lamb shank biryani, slow-cooked with caramelised onions, saffron &amp; spices – rich and aromatic.</p></div>
    </div>
  </div>

  <div class="col plain" style="left:286px;top:30px;width:260px">
    <div class="menu-section">
      <h2>Breads</h2>
      <div class="item"><div class="item__line"><span>Classic Butter Naan</span><span class="item__leader"></span><span>$6</span></div><p class="item__desc">Soft, fluffy tandoor-baked bread brushed with butter.</p></div>
      <div class="item"><div class="item__line"><span>Garlic Naan</span><span class="item__leader"></span><span>$7</span></div><p class="item__desc">Tandoor-baked naan with fresh garlic &amp; coriander.</p></div>
      <div class="item"><div class="item__line"><span>Lachha Paratha</span><span class="item__leader"></span><span>$8</span></div><p class="item__desc">Crisp, flaky, multi-layered paratha pan-fried with ghee.</p></div>
      <div class="item"><div class="item__line"><span>Cheese Naan</span><span class="item__leader"></span><span>$8</span></div><p class="item__desc">Stuffed with molten cheese, baked in the tandoor.</p></div>
      <div class="item"><div class="item__line"><span>Cheese Garlic Naan</span><span class="item__leader"></span><span>$8.50</span></div><p class="item__desc">Naan layered with garlic &amp; cheese — indulgent &amp; aromatic.</p></div>
    </div>
  </div>

  <div class="col plain" style="left:286px;top:206px;width:260px">
    <div class="menu-section">
      <h2>Sides</h2>
      <div class="item"><div class="item__line"><span>Cucumber Raita</span><span class="item__leader"></span><span>$6</span></div><p class="item__desc">Cool yogurt with cucumber, cumin &amp; mint.</p></div>
      <div class="item"><div class="item__line"><span>Roasted Papadum</span><span class="item__leader"></span><span>$4 (4 pcs)</span></div><p class="item__desc">Crispy lentil wafers roasted for a healthy crunch.</p></div>
      <div class="item"><div class="item__line"><span>Masala Papad</span><span class="item__leader"></span><span>$8 (2 pcs)</span></div><p class="item__desc">Papad topped with spiced onions, tomatoes &amp; herbs.</p></div>
      <div class="item"><div class="item__line"><span>Onion Salad</span><span class="item__leader"></span><span>$6</span></div><p class="item__desc">Fresh onion rings tossed with lime &amp; masala.</p></div>
      <div class="item"><div class="item__line"><span>Garden Salad</span><span class="item__leader"></span><span>$8</span></div><p class="item__desc">Seasonal greens dressed with lemon &amp; cumin.</p></div>
      <div class="item"><div class="item__line" style="width:82%"><span>Mango Chutney / Mint Chutney / Mixed Pickle</span><span class="item__leader" style="border:0"></span><span>$4</span></div><p class="item__desc">House-made condiments to complement your meal.</p></div>
    </div>
  </div>

  <div class="col plain" style="left:286px;top:442px;width:260px">
    <div class="menu-section">
      <h2>Desserts</h2>
      <div class="item"><div class="item__line"><span>Kunafa Nest Gulab Jamun with Rabri</span><span class="item__leader"></span><span>$20</span></div><p class="item__desc">Golden kunafa nest cradling soft gulab jamun, draped in creamy rabri &amp; pistachios.</p></div>
      <div class="item"><div class="item__line"><span>Mango Mousse Delight</span><span class="item__leader"></span><span>$20</span></div><p class="item__desc">Alphonso mango mousse layered with coconut crumble &amp; fresh mint.</p></div>
      <div class="item"><div class="item__line"><span>Kulfi Falooda Trio</span><span class="item__leader"></span><span>$20</span></div><p class="item__desc">Traditional kulfi in pistachio, rose &amp; saffron, served with silky falooda.</p></div>
    </div>
  </div>
</section>

<section class="sheet sheet--inside">
  <div class="panel-chilli"></div>
  <div class="panel-leaf"></div>
  <div class="snack-photo" role="img" aria-label="Golden fried samosas on a wooden plate with mint chutney and tomato dip"></div>

  <div class="col on-dark" style="left:19px;top:30px;width:245px">
    <div class="menu-section">
      <h2>Vegetarian Entrées</h2>
      <div class="item"><div class="item__line"><span>Classic Samosa</span><span class="item__leader"></span><span>$16</span></div><p class="item__desc">Handcrafted pastry parcels filled with spiced potatoes &amp; peas, served with a duo of fresh mint-coriander chutney and sweet mango relish.</p></div>
      <div class="item"><div class="item__line"><span>Crispy Onion &amp; Spinach Bhaji</span><span class="item__leader"></span><span>$16</span></div><p class="item__desc">Crisp golden fritters of baby spinach &amp; onion, delicately spiced, paired with house chutneys.</p></div>
      <div class="item"><div class="item__line"><span>Harabhara Edamame Kebab</span><span class="item__leader"></span><span>$18</span></div><p class="item__desc">Pan-seared medallions of edamame and garden vegetables, stuffed with soft cheese and herbs, served with tangy yogurt dip.</p></div>
      <div class="item"><div class="item__line"><span>Zafrani Paneer Tikka</span><span class="item__leader"></span><span>$22</span></div><p class="item__desc">Cubes of cottage cheese marinated in saffron, cardamom &amp; smoky tandoor spices, grilled to perfection, served with mint chutney and microgreens.</p></div>
      <div class="item"><div class="item__line"><span>Vada Pav Sliders</span><span class="item__leader"></span><span>$16</span></div><p class="item__desc">A gourmet take on Mumbai's street legend: spiced potato croquette in a butter brioche bun, layered with tamarind, mint-coriander chutney &amp; fiery thecha, accompanied by crisp fried green chilli.</p></div>
    </div>
  </div>

  <div class="col" style="left:19px;top:314px;width:245px">
    <div class="menu-section">
      <h2>Non-Vegetarian Entrées</h2>
      <div class="item"><div class="item__line"><span>Smoke Tandoori Chicken Tikka</span><span class="item__leader"></span><span>$20</span></div><p class="item__desc">Charcoal-grilled chicken marinated overnight with aromatic spices, finished with a touch of smokey infusion.</p></div>
      <div class="item"><div class="item__line"><span>Chicken Malai Tikka</span><span class="item__leader"></span><span>$20</span></div><p class="item__desc">Tender chicken morsels marinated in cream, cheese &amp; cardamom, cooked gently in the tandoor for a melt-in-mouth experience.</p></div>
      <div class="item"><div class="item__line"><span>Awadhi Fish Tikka</span><span class="item__leader"></span><span>$22</span></div><p class="item__desc">Fresh barramundi fillets marinated with hand-pounded Awadhi spices, grilled for a delicate smokey finish.</p></div>
      <div class="item"><div class="item__line"><span>Tandoori Tiger Prawns</span><span class="item__leader"></span><span>$24</span></div><p class="item__desc">Jumbo prawns infused with curry-leaf butter, garlic &amp; chilli, char-grilled for an indulgent coastal flavour.</p></div>
      <div class="item"><div class="item__line"><span>Lamb Gilafi Seekh</span><span class="item__leader"></span><span>$22</span></div><p class="item__desc">Minced lamb spiced with herbs, peppers &amp; aromatics, skewered &amp; flame-roasted, served with minted yogurt.</p></div>
      <div class="item"><div class="item__line"><span>Tandoori Platter</span><span class="item__leader"></span><span>$39</span></div><p class="item__desc">A chef's selection of smoky tandoori classics: Chicken Tikka, Malai Tikka, Lamb Seekh &amp; Awadhi Fish, presented with a medley of chutneys &amp; dips.</p></div>
    </div>
  </div>

  <div class="col" style="left:290px;top:34px;width:255px">
    <div class="menu-section">
      <h2>Chaat</h2>
      <div class="item"><div class="item__line"><span>Panipuri Experience</span><span class="item__leader"></span><span>$20</span></div><p class="item__desc">Crisp puris filled with spiced potato, tangy chutneys &amp; chilled spiced water – a refined version of the street favourite.</p></div>
      <div class="item"><div class="item__line"><span>Burrata Chaat</span><span class="item__leader"></span><span>$20</span></div><p class="item__desc">Creamy burrata resting on crispy papdi, layered with tamarind glaze, mint chutney &amp; golden sev.</p></div>
      <div class="item"><div class="item__line"><span>Deconstructed Samosa Chaat</span><span class="item__leader"></span><span>$18</span></div><p class="item__desc">Crispy samosa pastry crumbles over spiced potato &amp; peas, dressed with chutneys, yogurt &amp; pomegranate jewels.</p></div>
    </div>
  </div>

  <div class="col" style="left:290px;top:324px;width:255px">
    <div class="menu-section">
      <h2>Classic Curries</h2>
      <div class="item"><div class="item__line"><span>Paneer / Kofta / Mixed Veg</span><span class="item__leader"></span><span>$26</span></div><p class="item__desc">Choose your protein with a choice of gourmet curry bases.</p></div>
      <div class="item"><div class="item__line"><span>Chicken / Lamb</span><span class="item__leader"></span><span>$28</span></div><p class="item__desc">Choose your protein with a choice of gourmet curry bases.</p></div>
      <div class="item"><div class="item__line"><span>Prawns / Fish</span><span class="item__leader"></span><span>$30</span></div><p class="item__desc">Choose your protein with a choice of gourmet curry bases.</p></div>
      <div class="item"><div class="item__line"><span>Vindaloo</span></div><p class="item__desc">Fiery Goan-style curry with red chillies &amp; vinegar.</p></div>
      <div class="item"><div class="item__line"><span>Saag</span></div><p class="item__desc">Creamy buttered spinach slow-cooked with spices.</p></div>
      <div class="item"><div class="item__line"><span>Korma</span></div><p class="item__desc">Mild, creamy cashew &amp; saffron curry.</p></div>
      <div class="item"><div class="item__line"><span>Masala</span></div><p class="item__desc">Tomato &amp; onion base enriched with cream &amp; butter.</p></div>
      <div class="item"><div class="item__line"><span>Madras</span></div><p class="item__desc">Coconut-based curry with onions, garlic &amp; curry leaves.</p></div>
    </div>
  </div>

  <div class="col" style="left:569px;top:34px;width:246px">
    <div class="menu-section">
      <h2>Indo-Chinese</h2>
      <div class="item"><div class="item__line"><span>Vegetable Manchurian Dry</span><span class="item__leader"></span><span>$22</span></div><p class="item__desc">Golden-fried vegetable dumplings wok-tossed in garlic, chilli &amp; soy glaze.</p></div>
      <div class="item"><div class="item__line"><span>Paneer Chilli Dry</span><span class="item__leader"></span><span>$24</span></div><p class="item__desc">Cottage cheese cubes tossed with peppers, onions &amp; chilli-garlic soy reduction.</p></div>
      <div class="item"><div class="item__line"><span>Chilli Chicken Dry</span><span class="item__leader"></span><span>$26</span></div><p class="item__desc">Tender chicken tossed with shallots, peppers &amp; fiery Indo-Chinese sauce.</p></div>
      <div class="item plain"><div class="item__line" style="width:92%"><span>Oriental Noodles</span><span class="item__leader"></span><span>Veg $22 / Chicken $24</span></div><p class="item__desc">Stir-fried noodles with seasonal vegetables, wok-seared with soy &amp; garlic.</p></div>
    </div>
  </div>

  <div class="col on-dark" style="left:569px;top:235px;width:246px">
    <div class="menu-section">
      <h2>Tulsi's Kitchen Special Vegetarian Curries</h2>
      <div class="item"><div class="item__line"><span>Sham Savera Kofta</span><span class="item__leader"></span><span>$26</span></div><p class="item__desc">Spinach dumplings filled with cottage cheese, simmered in a rich tomato-butter sauce – a true royal delicacy.</p></div>
      <div class="item"><div class="item__line"><span>Mexican Salsa Paneer</span><span class="item__leader"></span><span>$28</span></div><p class="item__desc">Paneer cubes tossed in a fusion of roasted Mexican-style tomato salsa and Indian spices – a bold East-meets-West creation.</p></div>
      <div class="item"><div class="item__line"><span>Mushroom Mutter Masala</span><span class="item__leader"></span><span>$26</span></div><p class="item__desc">Tender mushrooms and garden peas in a spiced onion-tomato gravy, finished with cream.</p></div>
      <div class="item"><div class="item__line"><span>Kaju Curry</span><span class="item__leader"></span><span>$28</span></div><p class="item__desc">A luxurious cashew-based curry enriched with aromatic spices, velvety texture &amp; buttery finish.</p></div>
      <div class="item"><div class="item__line"><span>Cheese Butter Masala</span><span class="item__leader"></span><span>$28</span></div><p class="item__desc">Paneer and soft cheese in a creamy, butter-rich tomato gravy – indulgent &amp; comforting.</p></div>
      <div class="item"><div class="item__line"><span>Dal Tadka</span><span class="item__leader"></span><span>$22</span></div><p class="item__desc">Yellow lentils tempered with garlic, cumin &amp; chilli, offering homestyle comfort with gourmet finesse.</p></div>
      <div class="item"><div class="item__line"><span>Dal Makhani</span><span class="item__leader"></span><span>$22</span></div><p class="item__desc">Black lentils, slow-cooked overnight with butter and cream – a timeless Delhi specialty.</p></div>
      <div class="item"><div class="item__line"><span>Vegetable Dum Biryani</span><span class="item__leader"></span><span>$28</span></div><p class="item__desc">Saffron-scented basmati rice layered with seasonal vegetables, sealed and slow-cooked in the dum style, served with cooling raita.</p></div>
    </div>
  </div>
</section>

</body>
</html>
```